Cookbook Cover Templates
Hearthside Recipe Binder
Cookbook Cover Templates - Publishing
Creative Brief
We are looking for a series of 3 cookbook cover templates along with matching section dividers that can be made available to editors looking to publish a personal or family cookbook.
Publishing
The typical cookbook writer is an American or Canadian female, age 25-50. We have several current covers available at: http://www.hearthsiderecipebinder.net/home2012/view_covers.asp Here are the current dividers available: http://www.hearthsiderecipebinder.net/home2012/view_dividers.asp We are looking for something with a sleek and modern feel, but still fun and food related. It least one of the covers needs to feature various cookies as a theme.
The images needs to be designed so that the text of the cookbook can be added later by the system. See current covers and dividers for examples. Your images should be 300dpi resolution. Full page with Bleed Custom Covers and Dividers must be sized at 6"x9" with 4.75"x7.75" active content or 1800 x 2700 pixels. Full page non-bleed Dividers and other images must be sized at 5.5"x8.5" with 4.75"x7.75" active content or 1650 x 2550 pixels It least one of the covers needs to have "cookies" as a theme. Dividers should relate to the cover and be black and white.

```html
<!DOCTYPE html>
<html lang="en">
<head>
<meta charset="utf-8">
<title>Cookbook Cover Templates</title>
<link href="https://fonts.googleapis.com/css2?family=Coustard:wght@900&family=Varela+Round&family=Cherry+Swash:wght@700&family=Arimo:ital@0;1&display=swap" rel="stylesheet">
<style>
  :root {
    --backdrop-light: #fbe4ec;
    --backdrop-mid: #f4c6d6;
    --cookie-frame: #c9a27c;
    --cookie-brown: #4a2a16;
    --cookie-purple: #8f2a8c;
    --cookie-photo-light: #f3ece4;
    --cookie-photo-dark: #c98a3e;
    --pasta-black: #050505;
    --pasta-glow: #b5571a;
    --pasta-deep: #2a0f04;
    --pasta-white: #ffffff;
    --cupcake-frame: #ec7aa2;
    --cupcake-purple: #7a2a8f;
    --cupcake-pink: #e2407e;
    --cupcake-blue: #2a8fd8;
    --cupcake-photo-light: #cfeef0;
    --cupcake-photo-pink: #f2a0bf;
    --ribbon: #f7bcd1;
    --page: #ffffff;
  }
  html, body { margin: 0; padding: 0; overflow: hidden; }
  .canvas {
    position: relative;
    width: 1200px;
    height: 871px;
    overflow: hidden;
    background: linear-gradient(180deg, var(--backdrop-light), var(--backdrop-mid) 50%, var(--backdrop-light));
  }
  .cover { position: absolute; box-sizing: border-box; }

  /* Cookie cover */
  .cover--cookie {
    left: 24px; top: 120px; width: 360px; height: 600px;
    background: var(--cookie-frame);
    padding: 22px;
  }
  .cover__page {
    position: relative; width: 100%; height: 100%;
    background: var(--page); overflow: hidden;
  }
  .cookie-title {
    position: absolute; left: 18px; top: 26px; margin: 0;
    font-family: "Coustard", Georgia, serif; font-weight: 900;
    line-height: 0.9;
  }
  .cookie-title__top { display: block; color: var(--cookie-brown); font-size: 78px; }
  .cookie-title__bottom { display: block; color: var(--cookie-purple); font-size: 62px; padding-left: 40px; }
  .cookie-photo {
    position: absolute; left: 0; right: 0; top: 178px; height: 240px;
    background: radial-gradient(ellipse at 45% 60%, var(--cookie-photo-dark) 0%, #deb680 35%, var(--cookie-photo-light) 70%);
  }
  .wording {
    position: absolute; left: 0; right: 0; text-align: center;
    font-family: "Arimo", Arial, sans-serif; font-size: 21px; margin: 0;
  }
  .cover--cookie .wording--first { top: 468px; color: var(--cookie-brown); }
  .cover--cookie .wording--second { top: 498px; color: var(--cookie-purple); }

  /* Pasta cover */
  .cover--pasta {
    left: 396px; top: 106px; width: 396px; height: 614px;
    background: var(--pasta-black);
  }
  .pasta-title {
    position: absolute; left: 0; right: 0; top: 42px; margin: 0;
    text-align: center; color: var(--pasta-white);
    font-family: "Varela Round", Verdana, sans-serif; font-size: 54px; letter-spacing: 2px;
  }
  .pasta-subtitle {
    position: absolute; left: 0; right: 0; top: 112px; margin: 0;
    text-align: center; color: var(--pasta-white);
    font-family: "Arimo", Arial, sans-serif; font-style: italic; font-size: 14px;
  }
  .pasta-photo {
    position: absolute; left: 0; right: 0; top: 140px; height: 380px;
    background: radial-gradient(ellipse at 55% 45%, var(--pasta-glow) 0%, #7a300c 30%, var(--pasta-deep) 60%, var(--pasta-black) 85%);
  }
  .pasta-label {
    position: absolute; left: 0; right: 0; top: 546px; margin: 0;
    text-align: center; color: var(--pasta-white);
    font-family: "Varela Round", Verdana, sans-serif; font-size: 32px; letter-spacing: 1px;
  }

  /* Cupcake cover */
  .cover--cupcake {
    left: 804px; top: 120px; width: 372px; height: 600px;
    background: var(--cupcake-frame);
    padding: 22px;
  }
  .cupcake-title {
    position: absolute; left: 0; right: 0; top: 20px; margin: 0;
    text-align: center; font-family: "Cherry Swash", Georgia, serif; font-weight: 700;
    font-size: 50px; line-height: 1;
  }
  .cupcake-title__top { display: block; color: var(--cupcake-purple); }
  .cupcake-title__bottom { display: block; color: var(--cupcake-pink); }
  .cupcake-photo {
    position: absolute; left: 0; right: 0; top: 124px; height: 258px;
    background: linear-gradient(180deg, var(--cupcake-photo-light) 0%, #e6f4f3 40%, var(--cupcake-photo-pink) 75%, #f7d6e2 100%);
  }
  .ribbon {
    position: absolute; left: 0; right: 0; top: 400px; height: 26px;
    background: var(--ribbon);
  }
  .cover--cupcake .wording--first { top: 462px; color: var(--cupcake-blue); }
  .cover--cupcake .wording--second { top: 492px; color: var(--cupcake-pink); }
</style>
</head>
<body>
<main class="canvas">

  <section class="cover cover--cookie">
    <div class="cover__page">
      <h2 class="cookie-title">
        <span class="cookie-title__top">Cook</span>
        <span class="cookie-title__bottom">bookie</span>
      </h2>
      <div class="cookie-photo" role="img" aria-label="Photo of stacked chocolate chip cookies with chocolate pieces"></div>
      <p class="wording wording--first">your wording goes here</p>
      <p class="wording wording--second">change top &amp; bottom</p>
    </div>
  </section>

  <section class="cover cover--pasta">
    <h2 class="pasta-title">Cookbook</h2>
    <p class="pasta-subtitle">Your wording goes here</p>
    <div class="pasta-photo" role="img" aria-label="Photo of a plate of penne pasta in tomato sauce with basil and a fork"></div>
    <p class="pasta-label">Special Pasta</p>
  </section>

  <section class="cover cover--cupcake">
    <div class="cover__page">
      <h2 class="cupcake-title">
        <span class="cupcake-title__top">Cupcook</span>
        <span class="cupcake-title__bottom">Cupbook</span>
      </h2>
      <div class="cupcake-photo" role="img" aria-label="Photo of pink frosted cupcakes topped with sugar roses"></div>
      <div class="ribbon"></div>
      <p class="wording wording--first">your wording goes here</p>
      <p class="wording wording--second">change top &amp; bottom</p>
    </div>
  </section>

</main>
</body>
</html>
```